Next-Gen B2B Sales Negotiation App - UI Design for iOS

Develop a user-friendly dark-mode interface for a B2B sales negotiation assistant app for a company called Quorvel. The UI will showcase a single screen with features like counterparty search, agenda selection, and email drafting. Design should reflect a functional iOS app with realistic placeholder data to create a genuine experience.

Precise task description in attachment.

Target Market(s)

B2B

Requirements
Must have
• Each UI picture should look like a screen capture of an iphone
Nice to have
• The UI designs need to show the navigation and the app in use

```html
<!DOCTYPE html>
<html lang="en">
<head>
<meta charset="utf-8">
<title>Quorvel Assistant – Negotiation Screens</title>
<link href="https://fonts.googleapis.com/css2?family=Plus+Jakarta+Sans:wght@400;500;600;700&display=swap" rel="stylesheet">
<style>
:root{
  --canvas:#8e8f95;
  --panel:#161618;
  --panel-deep:#050506;
  --card:#1d1d20;
  --card-2:#222226;
  --line:#2c2c31;
  --text:#f4f4f6;
  --muted:#8e8e97;
  --dim:#6b6b73;
  --pink:#ec4f93;
  --pink-2:#e0405f;
  --purple:#8b3fe0;
  --green:#4fd27a;
  --green-bg:#15301f;
  --cyan:#6fd3e6;
}
*{box-sizing:border-box;margin:0;padding:0}
html,body{width:1200px;height:1200px;overflow:hidden}
body{background:var(--canvas);font-family:"Plus Jakarta Sans",sans-serif;color:var(--text);position:relative}
.abs{position:absolute}
.panel{position:absolute;background:var(--panel);border-radius:25px;overflow:hidden}
.panel.deep{background:var(--panel-deep)}
.label{position:absolute;font-size:9px;letter-spacing:.06em;text-transform:uppercase;color:var(--muted);line-height:12px}
.label.pink{color:var(--pink)}
.value{position:absolute;font-size:13px;line-height:16px;color:var(--text)}
.value.lg{font-size:15px;line-height:18px;font-weight:500}
.value.bold{font-weight:700}
.rule{position:absolute;height:1px;background:var(--line)}
.card{position:absolute;background:var(--card);border:1px solid var(--line);border-radius:8px}
.segment{position:absolute;background:var(--card-2);border-radius:7px}
.pill{position:absolute;background:var(--pink);border-radius:6px;box-shadow:0 4px 14px rgba(236,79,147,.35)}
.seg-text{position:absolute;font-size:9.5px;font-weight:600;letter-spacing:.08em;text-transform:uppercase;color:var(--muted);line-height:12px;transform:translateX(-50%);white-space:nowrap;display:flex;align-items:center;gap:6px}
.seg-text.on{color:#fff}
.section-title{position:absolute;display:flex;align-items:center;gap:8px;font-size:13.5px;font-weight:600;line-height:18px}
.badge{position:absolute;background:var(--green-bg);border:1px solid #2e6b40;color:var(--green);border-radius:5px;font-size:8.5px;font-weight:700;letter-spacing:.04em;display:flex;align-items:center;justify-content:center}
.avatar{position:absolute;width:35px;height:35px;border-radius:7px;background:linear-gradient(145deg,#ec4f93,#5a2240);display:flex;align-items:center;justify-content:center;font-weight:700;font-size:14px;box-shadow:0 4px 12px rgba(236,79,147,.3)}
.brand{position:absolute;font-size:17px;font-weight:700;line-height:20px}
.brand-sub{position:absolute;font-size:9px;letter-spacing:.16em;color:var(--muted);line-height:11px}
.more{position:absolute;width:31px;height:31px;border-radius:6px;background:#242428;display:flex;align-items:center;justify-content:center}
.tag{position:absolute;height:25px;border:1px solid var(--line);background:#1b1b1e;border-radius:5px;font-size:11px;display:flex;align-items:center;justify-content:center;color:#e6e6ea}
.tag.dashed{border:1px dashed #45454c;background:transparent;color:var(--muted);font-size:9px;font-weight:600;letter-spacing:.08em}
.btn{position:absolute;display:flex;align-items:center;justify-content:center;font-size:11px;font-weight:600;border-radius:4px}
.btn.primary{background:var(--pink);color:#fff}
.btn.ghost{color:#d0d0d6}
.modal{position:absolute;background:#1b1b1e;border:1px solid #2e2e33;border-radius:4px}
.modal-title{position:absolute;width:100%;text-align:center;font-size:18px;font-weight:700;line-height:22px}
.modal-sub{position:absolute;width:100%;text-align:center;font-size:10px;color:var(--muted);line-height:13px}
.row-key{position:absolute;font-size:10px;font-weight:600;letter-spacing:.05em;color:#7d7d86;line-height:13px}
.row-val{position:absolute;font-size:12px;font-weight:600;line-height:15px;text-align:right}
.menu{position:absolute;background:#1e1e21;border:1px solid #323237;border-radius:6px;box-shadow:0 10px 30px rgba(0,0,0,.5)}
.menu-item{position:absolute;left:14px;display:flex;align-items:center;gap:10px;font-size:11.5px;line-height:14px;color:#e8e8ec}
.option{position:absolute;font-size:11px;line-height:14px;color:#b9b9c0}
svg{display:block}
</style>
</head>
<body>

<!-- Main composer screen -->
<section class="panel" style="left:45px;top:32px;width:346px;height:1080px">
  <div class="avatar" style="left:22px;top:29px">Q</div>
  <div class="brand" style="left:68px;top:32px">Quorvel</div>
  <div class="brand-sub" style="left:68px;top:52px">ASSISTANT</div>
  <div class="more" style="left:296px;top:31px"><svg width="4" height="14"><circle cx="2" cy="2" r="1.4" fill="#ccc"/><circle cx="2" cy="7" r="1.4" fill="#ccc"/><circle cx="2" cy="12" r="1.4" fill="#ccc"/></svg></div>
  <div class="rule" style="left:0;top:79px;width:346px"></div>

  <div class="segment" style="left:19px;top:94px;width:311px;height:37px"></div>
  <div class="pill" style="left:22px;top:97px;width:101px;height:31px"></div>
  <div class="seg-text on" style="left:73px;top:107px">Company</div>
  <div class="seg-text" style="left:175px;top:107px">Individual</div>
  <div class="seg-text" style="left:277px;top:107px">Group</div>

  <div class="section-title" style="left:22px;top:147px"><svg width="14" height="14" viewBox="0 0 24 24" fill="none" stroke="var(--cyan)" stroke-width="2"><circle cx="9" cy="8" r="4"/><path d="M2 21c0-4 3-7 7-7s7 3 7 7"/><path d="M16 4a4 4 0 0 1 0 8M18 14c2.5 1 4 3.5 4 7"/></svg>Target Profile</div>
  <div class="badge" style="left:270px;top:146px;width:57px;height:18px">VERIFIED</div>

  <div class="card" style="left:19px;top:180px;width:311px;height:143px"></div>
  <div class="label" style="left:37px;top:198px">Name / Entity</div>
  <div class="value lg" style="left:37px;top:217px">Norbeck Ltd.</div>
  <svg class="abs" style="left:299px;top:219px" width="14" height="14" viewBox="0 0 24 24" fill="none" stroke="var(--cyan)" stroke-width="2.2"><circle cx="11" cy="11" r="7"/><path d="M20 20l-4-4"/></svg>
  <div class="rule" style="left:37px;top:243px;width:275px"></div>
  <div class="label" style="left:37px;top:262px">Role / Context</div>
  <div class="value" style="left:37px;top:279px">Lena Marsh (CEO)</div>
  <div class="rule" style="left:37px;top:303px;width:275px"></div>

  <div class="section-title" style="left:22px;top:339px"><svg width="14" height="14" viewBox="0 0 24 24" fill="none" stroke="var(--cyan)" stroke-width="2"><circle cx="12" cy="12" r="9"/><path d="M12 2v5M12 17v5M2 12h5M17 12h5"/></svg>Strategy</div>

  <div class="card" style="left:19px;top:371px;width:311px;height:138px"></div>
  <div class="label pink" style="left:37px;top:391px">Current Objective</div>
  <div class="value lg bold" style="left:37px;top:409px">Book a Meeting</div>
  <svg class="abs" style="left:297px;top:405px" width="12" height="8" viewBox="0 0 12 8" fill="none" stroke="#9a9aa2" stroke-width="1.6"><path d="M1 1l5 5 5-5"/></svg>
  <div class="rule" style="left:19px;top:443px;width:311px"></div>
  <div class="abs" style="left:174px;top:443px;width:1px;height:66px;background:var(--line)"></div>
  <div class="label" style="left:37px;top:459px">Duration</div>
  <div class="value bold" style="left:37px;top:475px;display:flex;gap:8px;align-items:center;font-size:13.5px"><svg width="12" height="12" viewBox="0 0 24 24" fill="none" stroke="var(--cyan)" stroke-width="2.4"><circle cx="12" cy="12" r="9"/><path d="M12 7v5l3 2"/></svg>45 min</div>
  <div class="label" style="left:188px;top:459px">Target Date</div>
  <div class="value bold" style="left:188px;top:475px;display:flex;gap:8px;align-items:center;font-size:13.5px"><svg width="12" height="12" viewBox="0 0 24 24" fill="none" stroke="var(--pink)" stroke-width="2.4"><rect x="3" y="5" width="18" height="16" rx="2"/><path d="M3 10h18M8 3v4M16 3v4"/></svg>25/01/2025</div>

  <div class="segment" style="left:19px;top:538px;width:311px;height:40px"></div>
  <div class="pill" style="left:22px;top:541px;width:152px;height:34px"></div>
  <div class="seg-text on" style="left:98px;top:552px"><svg width="12" height="10" viewBox="0 0 24 18" fill="none" stroke="#fff" stroke-width="2.2"><rect x="1" y="2" width="15" height="14" rx="2"/><path d="M16 7l6-3v10l-6-3"/></svg>Online</div>
  <div class="seg-text" style="left:252px;top:552px"><svg width="10" height="12" viewBox="0 0 20 24" fill="none" stroke="#9a9aa2" stroke-width="2.2"><path d="M10 22s8-7 8-13a8 8 0 0 0-16 0c0 6 8 13 8 13z"/><circle cx="10" cy="9" r="3"/></svg>On-Site</div>

  <div class="tag" style="left:19px;top:597px;width:73px">Save Time</div>
  <div class="tag" style="left:100px;top:597px;width:113px">Increase Revenue</div>
  <div class="tag dashed" style="left:212px;top:597px;width:73px">+ ADD TAG</div>
  <div class="seg-text" style="left:313px;top:604px">Clear</div>

  <div class="card" style="left:19px;top:656px;width:311px;height:306px;overflow:hidden"><div style="height:3px;background:linear-gradient(90deg,var(--pink),var(--purple))"></div></div>
  <div class="segment" style="left:37px;top:678px;width:100px;height:36px;background:#27272b"></div>
  <div class="pill" style="left:40px;top:681px;width:29px;height:29px;display:flex;align-items:center;justify-content:center"><svg width="13" height="10" viewBox="0 0 26 20" fill="none" stroke="#fff" stroke-width="2.4"><rect x="1" y="1" width="24" height="18" rx="2"/><path d="M1 3l12 9 12-9"/></svg></div>
  <div class="abs" style="left:75px;top:689px;font-size:9px;font-weight:600;color:#b9b9c0">Linko</div>
  <svg class="abs" style="left:112px;top:689px" width="13" height="13" viewBox="0 0 24 24" fill="none" stroke="#b9b9c0" stroke-width="2"><path d="M5 3h4l2 5-3 2a11 11 0 0 0 6 6l2-3 5 2v4a2 2 0 0 1-2 2A17 17 0 0 1 3 5a2 2 0 0 1 2-2z"/></svg>
  <div class="abs" style="right:34px;top:690px;font-size:9.5px;font-weight:700;letter-spacing:.04em;color:var(--pink);display:flex;align-items:center;gap:4px"><svg width="11" height="11" viewBox="0 0 24 24" fill="none" stroke="var(--pink)" stroke-width="2"><path d="M12 3l2 6 6 2-6 2-2 6-2-6-6-2 6-2z"/></svg>AI IMPROVE</div>
  <div class="label" style="left:37px;top:764px;top:732px">Subject</div>
  <div class="value bold" style="left:37px;top:747px;font-size:11px">Proposed Meeting: Norbeck Ltd. x Quorvel</div>
  <div class="rule" style="left:37px;top:769px;width:275px"></div>
  <div class="abs" style="left:37px;top:784px;font-size:10px;color:var(--muted)">Hi Lena,</div>
  <div class="abs" style="left:37px;top:803px;width:280px;font-size:12.6px;line-height:20.3px;color:#e8e8ec">I would like to discuss how Quorvel can help you save time with automated negotiations. I propose a quick 30 min online meeting on Tuesday. Looking forward to your response.</div>
  <div class="rule" style="left:37px;top:906px;width:275px"></div>
  <div class="tag" style="left:37px;top:918px;width:109px;font-size:9.5px;gap:6px"><svg width="9" height="11" viewBox="0 0 18 22" fill="none" stroke="var(--pink)" stroke-width="2"><path d="M2 1h9l5 5v15H2z"/><path d="M5 11h8M5 15h8"/></svg>Proposal_v1.pdf</div>

  <div class="rule" style="left:0;top:1009px;width:346px"></div>
  <svg class="abs" style="left:35px;top:1028px" width="20" height="20" viewBox="0 0 24 24" fill="none" stroke="#b9b9c0" stroke-width="1.8"><rect x="2" y="4" width="16" height="16" rx="2"/><path d="M2 9h16M6 2v4M14 2v4"/><circle cx="17" cy="17" r="5" fill="var(--panel)"/><path d="M17 15v2l1.5 1"/></svg>
  <div class="abs" style="left:44px;top:1054px;transform:translateX(-50%);font-size:8px;font-weight:600;letter-spacing:.08em;color:#c9c9cf">SCHEDULE</div>
  <div class="btn primary" style="left:81px;top:1025px;width:247px;height:42px;font-size:13px;border-radius:5px;background:linear-gradient(90deg,var(--pink),var(--pink-2));gap:8px">Send Request <svg width="12" height="10" viewBox="0 0 24 20" fill="none" stroke="#fff" stroke-width="2.4"><path d="M2 10h19M13 2l8 8-8 8"/></svg></div>
</section>

<!-- Search focus state -->
<section class="panel" style="left:427px;top:32px;width:346px;height:267px">
  <div class="segment" style="left:16px;top:17px;width:311px;height:38px"></div>
  <div class="pill" style="left:19px;top:21px;width:102px;height:31px"></div>
  <div class="seg-text on" style="left:70px;top:31px">Company</div>
  <div class="seg-text" style="left:172px;top:31px">Individual</div>
  <div class="seg-text" style="left:273px;top:31px">Group</div>
  <div class="section-title" style="left:19px;top:71px"><svg width="14" height="14" viewBox="0 0 24 24" fill="none" stroke="var(--cyan)" stroke-width="2"><circle cx="9" cy="8" r="4"/><path d="M2 21c0-4 3-7 7-7s7 3 7 7"/><path d="M16 4a4 4 0 0 1 0 8M18 14c2.5 1 4 3.5 4 7"/></svg>Target Profile</div>
  <div class="badge" style="left:268px;top:70px;width:57px;height:18px">VERIFIED</div>
  <div class="card" style="left:16px;top:103px;width:311px;height:143px"></div>
  <div class="label" style="left:35px;top:122px">Name / Entity</div>
  <div class="value lg" style="left:35px;top:140px">Norbeck Ltd.<span style="display:inline-block;width:1px;height:16px;background:#fff;vertical-align:middle;margin-left:1px"></span></div>
  <svg class="abs" style="left:296px;top:142px" width="14" height="14" viewBox="0 0 24 24" fill="none" stroke="var(--cyan)" stroke-width="2.2"><circle cx="11" cy="11" r="7"/><path d="M20 20l-4-4"/></svg>
  <div class="rule" style="left:35px;top:167px;width:275px;background:var(--pink)"></div>
  <div class="label" style="left:35px;top:186px">Role / Context</div>
  <div class="value" style="left:35px;top:203px">Lena Marsh (CEO)</div>
  <div class="rule" style="left:35px;top:227px;width:275px"></div>
</section>

<!-- Objective dropdown state -->
<section class="panel" style="left:427px;top:321px;width:346px;height:482px">
  <div class="section-title" style="left:19px;top:20px"><svg width="14" height="14" viewBox="0 0 24 24" fill="none" stroke="var(--cyan)" stroke-width="2"><circle cx="12" cy="12" r="9"/><path d="M12 2v5M12 17v5M2 12h5M17 12h5"/></svg>Strategy</div>
  <div class="card" style="left:16px;top:52px;width:311px;height:256px"></div>
  <div class="label pink" style="left:35px;top:71px">Current Objective</div>
  <div class="value lg bold" style="left:35px;top:90px">Book a Meeting</div>
  <svg class="abs" style="left:294px;top:86px" width="12" height="8" viewBox="0 0 12 8" fill="none" stroke="#9a9aa2" stroke-width="1.6"><path d="M1 7l5-5 5 5"/></svg>
  <div class="option" style="left:45px;top:141px;color:#f0f0f3">Technical Review</div>
  <svg class="abs" style="left:288px;top:143px" width="10" height="8" viewBox="0 0 10 8" fill="none" stroke="var(--cyan)" stroke-width="1.5"><path d="M1 4l3 3 5-6"/></svg>
  <div class="option" style="left:45px;top:173px">Product Negotiation</div>
  <div class="option" style="left:45px;top:205px">Partnership Proposal</div>
  <div class="rule" style="left:20px;top:240px;width:303px"></div>
  <div class="abs" style="left:171px;top:240px;width:1px;height:68px;background:var(--line)"></div>
  <div class="label" style="left:35px;top:256px">Duration</div>
  <div class="value bold" style="left:35px;top:273px;display:flex;gap:8px;align-items:center;font-size:13.5px"><svg width="12" height="12" viewBox="0 0 24 24" fill="none" stroke="var(--cyan)" stroke-width="2.4"><circle cx="12" cy="12" r="9"/><path d="M12 7v5l3 2"/></svg>45 min</div>
  <div class="label" style="left:186px;top:256px">Target Date</div>
  <div class="value bold" style="left:186px;top:273px;display:flex;gap:8px;align-items:center;font-size:13.5px"><svg width="12" height="12" viewBox="0 0 24 24" fill="none" stroke="var(--pink)" stroke-width="2.4"><rect x="3" y="5" width="18" height="16" rx="2"/><path d="M3 10h18M8 3v4M16 3v4"/></svg>25/01/2025</div>

  <div class="segment" style="left:16px;top:323px;width:311px;height:41px"></div>
  <div class="pill" style="left:172px;top:326px;width:152px;height:34px"></div>
  <div class="seg-text" style="left:95px;top:337px"><svg width="12" height="10" viewBox="0 0 24 18" fill="none" stroke="#9a9aa2" stroke-width="2.2"><rect x="1" y="2" width="15" height="14" rx="2"/><path d="M16 7l6-3v10l-6-3"/></svg>Online</div>
  <div class="seg-text on" style="left:248px;top:337px"><svg width="10" height="12" viewBox="0 0 20 24" fill="none" stroke="#fff" stroke-width="2.2"><path d="M10 22s8-7 8-13a8 8 0 0 0-16 0c0 6 8 13 8 13z"/><circle cx="10" cy="9" r="3"/></svg>On-Site</div>

  <div class="card" style="left:16px;top:378px;width:311px;height:37px;border-radius:6px"></div>
  <svg class="abs" style="left:32px;top:390px" width="12" height="12" viewBox="0 0 24 24" fill="none" stroke="var(--pink)" stroke-width="2.2"><path d="M22 2L2 10l9 3 3 9z"/></svg>
  <div class="value" style="left:55px;top:389px;font-size:11px">Main Office, Building A</div>
  <div class="tag dashed" style="left:23px;top:434px;width:75px">+ ADD TAG</div>
</section>

<!-- Account menu state -->
<section class="panel" style="left:427px;top:825px;width:346px;height:343px">
  <div class="avatar" style="left:19px;top:30px">Q</div>
  <div class="brand" style="left:66px;top:32px">Quorvel</div>
  <div class="brand-sub" style="left:66px;top:53px">ASSISTANT</div>
  <div class="more" style="left:292px;top:32px"><svg width="4" height="14"><circle cx="2" cy="2" r="1.4" fill="#ccc"/><circle cx="2" cy="7" r="1.4" fill="#ccc"/><circle cx="2" cy="12" r="1.4" fill="#ccc"/></svg></div>
  <div class="rule" style="left:0;top:81px;width:346px"></div>
  <div class="segment" style="left:16px;top:95px;width:311px;height:37px"></div>
  <div class="pill" style="left:121px;top:98px;width:102px;height:31px"></div>
  <div class="seg-text" style="left:70px;top:108px">Company</div>
  <div class="seg-text on" style="left:149px;top:108px">In</div>
  <div class="section-title" style="left:19px;top:147px"><svg width="14" height="14" viewBox="0 0 24 24" fill="none" stroke="var(--cyan)" stroke-width="2"><circle cx="9" cy="8" r="4"/><path d="M2 21c0-4 3-7 7-7s7 3 7 7"/><path d="M16 4a4 4 0 0 1 0 8M18 14c2.5 1 4 3.5 4 7"/></svg>Target Profile</div>
  <div class="card" style="left:16px;top:181px;width:311px;height:143px"></div>
  <div class="label" style="left:35px;top:200px">Name / Entity</div>
  <div class="value lg" style="left:35px;top:218px">Tobias Wren</div>
  <svg class="abs" style="left:296px;top:220px" width="14" height="14" viewBox="0 0 24 24" fill="none" stroke="var(--cyan)" stroke-width="2.2"><circle cx="11" cy="11" r="7"/><path d="M20 20l-4-4"/></svg>
  <div class="rule" style="left:35px;top:244px;width:275px"></div>
  <div class="label" style="left:35px;top:263px">Role / Context</div>
  <div class="value" style="left:35px;top:280px">Head of Engineering @ Fieldlark</div>
  <div class="rule" style="left:35px;top:304px;width:275px"></div>

  <div class="menu" style="left:154px;top:71px;width:170px;height:151px">
    <div class="menu-item" style="top:17px"><svg width="12" height="12" viewBox="0 0 24 24" fill="none" stroke="#cfcfd5" stroke-width="2"><circle cx="12" cy="8" r="4"/><path d="M4 22c0-4 4-7 8-7s8 3 8 7"/></svg>View Profile</div>
    <div class="menu-item" style="top:49px"><svg width="12" height="12" viewBox="0 0 24 24" fill="none" stroke="#cfcfd5" stroke-width="2"><path d="M3 12a9 9 0 1 0 3-6.7L3 8"/><path d="M3 3v5h5M12 7v5l3 2"/></svg>Negotiation History</div>
    <div class="menu-item" style="top:81px"><svg width="12" height="12" viewBox="0 0 24 24" fill="none" stroke="#cfcfd5" stroke-width="2"><circle cx="18" cy="5" r="3"/><circle cx="6" cy="12" r="3"/><circle cx="18" cy="19" r="3"/><path d="M8.6 10.5l6.8-4M8.6 13.5l6.8 4"/></svg>Export Strategy</div>
    <div class="rule" style="left:0;top:107px;width:168px"></div>
    <div class="menu-item" style="top:121px;color:var(--pink)"><svg width="12" height="12" viewBox="0 0 24 24" fill="none" stroke="var(--pink)" stroke-width="2"><path d="M9 3H4v18h5M16 17l5-5-5-5M21 12H9"/></svg>Sign Out</div>
  </div>
</section>

<!-- Schedule confirmation -->
<section class="panel deep" style="left:806px;top:32px;width:349px;height:367px">
  <div class="modal" style="left:25px;top:29px;width:297px;height:310px">
    <div class="modal-title" style="top:22px">Ready to Send?</div>
    <div class="modal-sub" style="top:48px">Review the details below</div>
    <div class="rule" style="left:0;top:81px;width:295px"></div>
    <div class="row-key" style="left:20px;top:104px">RECIPIENT</div>
    <div class="row-val" style="right:20px;top:103px">Global Ops Team</div>
    <div class="row-key" style="left:20px;top:135px">AGENDA</div>
    <div class="row-val" style="right:20px;top:134px">Product Demo</div>
    <div class="row-key" style="left:20px;top:178px;font-size:8.5px;color:var(--pink);letter-spacing:0">SCHEDULE TIME</div>
    <div class="abs" style="left:20px;top:198px;width:255px;height:30px;border:1px solid #34343a;background:#1f1f23;border-radius:4px;font-size:10.5px;color:#c9c9cf;display:flex;align-items:center;justify-content:space-between;padding:0 11px">dd/mm/yyyy --.-- <svg width="9" height="9" viewBox="0 0 24 24" fill="#c9c9cf"><rect x="3" y="5" width="18" height="16" rx="2"/></svg></div>
    <div class="btn ghost" style="left:37px;top:256px;width:90px;height:34px">Cancel</div>
    <div class="btn primary" style="left:153px;top:256px;width:122px;height:34px">Schedule</div>
  </div>
</section>

<!-- Send now confirmation -->
<section class="panel deep" style="left:806px;top:422px;width:349px;height:289px">
  <div class="modal" style="left:25px;top:28px;width:297px;height:234px">
    <div class="modal-title" style="top:23px">Ready to Send?</div>
    <div class="modal-sub" style="top:49px">Review the details below</div>
    <div class="rule" style="left:0;top:81px;width:295px"></div>
    <div class="row-key" style="left:20px;top:105px">RECIPIENT</div>
    <div class="row-val" style="right:20px;top:104px">Global Ops Team</div>
    <div class="row-key" style="left:20px;top:136px">AGENDA</div>
    <div class="row-val" style="right:20px;top:135px">Product Demo</div>
    <div class="btn ghost" style="left:37px;top:178px;width:90px;height:34px">Cancel</div>
    <div class="btn primary" style="left:153px;top:178px;width:122px;height:34px">Send Now</div>
  </div>
</section>

<!-- Success state -->
<section class="panel deep" style="left:806px;top:733px;width:349px;height:290px">
  <div class="abs" style="left:145px;top:63px;width:57px;height:56px;border:1px solid #3d8a55;background:var(--green-bg);border-radius:3px;display:flex;align-items:center;justify-content:center"><svg width="24" height="18" viewBox="0 0 24 18" fill="none" stroke="var(--green)" stroke-width="2.6"><path d="M2 9l7 7L22 2"/></svg></div>
  <div class="abs" style="left:0;width:349px;top:134px;text-align:center;font-size:22px;font-weight:700;line-height:28px">Sent Successfully</div>
  <div class="btn" style="left:131px;top:191px;width:89px;height:37px;border:1px solid #3a3a40;font-size:11.5px;color:#fff">Close</div>
</section>

</body>
</html>
```